Business Card Design Project

We are an incubator company that helps young entrepreneur to launch new ideas into the market. We will be targeting investors or likewise; Angels, young entrepreneurs and technopreneurs.

Our logo is being tasked by artflockly to design, therefore there is no logo for now.
You can us Lanternfold Pte Ltd as the logo for the time being.

Please let us have some versions of modern and yet professional designs; for words, you can indicate e.g (address), (Title)

thanks

Target Market(s)

young entrepreneurs
angels, investors

Industry/Entity Type

Business

Colors
3176b5
ffffff

Requirements
Must have
• able to project out our name; Lanternfold
Should not have
• Nothing childish or cartoon

```html
<!DOCTYPE html>
<html lang="en">
<head>
<meta charset="utf-8">
<title>Lanternfold Business Card</title>
<link rel="stylesheet" href="https://fonts.googleapis.com/css2?family=Questrial&display=swap">
<style>
  :root {
    --page: #ecebe8;
    --peach: #f6d1a3;
    --orange: #e98a20;
    --tan: #d7b48a;
    --leather-dark: #8e4322;
    --leather-light: #c4703f;
    --seam: #5a3418;
    --brand-blue: #29a8e0;
    --ink: #3a3a3a;
  }
  * { margin: 0; padding: 0; box-sizing: border-box; }
  html, body {
    width: 1200px; height: 1200px; overflow: hidden;
    background: var(--page);
    font-family: "Questrial", sans-serif;
  }
  .card {
    position: absolute; left: 220px;
    width: 760px; height: 434px;
    overflow: hidden;
    box-shadow: 0 6px 18px rgba(0,0,0,.18);
  }
  .card-back { top: 120px; background: var(--peach); }
  .card-front { top: 646px; }
  .card svg { position: absolute; inset: 0; }
  .brand-name {
    position: absolute;
    color: var(--brand-blue);
    text-transform: uppercase;
    white-space: nowrap;
  }
  .card-back .brand-name {
    left: 350px; top: 150px;
    font-size: 34px; letter-spacing: 1px;
  }
  .card-back .brand-rule {
    position: absolute; left: 350px; top: 198px;
    width: 262px; height: 3px; background: var(--ink);
  }
  .card-back .brand-dot {
    position: absolute; left: 459px; top: 80px;
    width: 44px; height: 44px; border-radius: 50%;
    background: var(--brand-blue);
  }
  .address {
    position: absolute; left: 150px; top: 322px;
    font-size: 19px; line-height: 1.35; color: var(--ink);
  }
  .card-front .brand-dot {
    position: absolute; left: 358px; top: 110px;
    width: 44px; height: 44px; border-radius: 50%;
    background: var(--brand-blue);
  }
  .card-front .brand-name {
    left: 0; right: 0; top: 190px; text-align: center;
    font-size: 62px; letter-spacing: 3px;
  }
</style>
</head>
<body>
  <section class="card card-back">
    <svg width="760" height="434" viewBox="0 0 760 434" aria-hidden="true">
      <path d="M0 0 H400 Q390 120 250 190 Q140 240 0 230 Z" fill="var(--orange)"/>
    </svg>
    <span class="brand-dot"></span>
    <div class="brand-name">Lanternfold</div>
    <span class="brand-rule"></span>
    <p class="address">57 Marlow Crescent<br>Eastvale 3310</p>
  </section>

  <section class="card card-front">
    <svg width="760" height="434" viewBox="0 0 760 434">
      <defs>
        <linearGradient id="leather" x1="0" y1="0" x2="1" y2="1">
          <stop offset="0" stop-color="var(--leather-light)"/>
          <stop offset="1" stop-color="var(--leather-dark)"/>
        </linearGradient>
      </defs>
      <rect width="760" height="434" fill="url(#leather)" role="img" aria-label="Pebbled football leather texture"/>
      <ellipse cx="380" cy="217" rx="600" ry="200" fill="var(--tan)" stroke="var(--seam)" stroke-width="7"/>
    </svg>
    <span class="brand-dot"></span>
    <div class="brand-name">Lanternfold</div>
  </section>
</body>
</html>
```